We need a design for our security installation based business. Our name is K M Security Systems

We need a business card for a security installation based company. We want to look modern and professional. We would like our company logo used and the three main colours to be white, black and orange. We install intruder alarms, cctv and access control. Our preference would be to use the black/orange design on the front and orange/black on the back. Feel free to post variations.

Target Market(s)

Business owners, commercial property and large residential properties

Industry/Entity Type

Business

Contact Information for Business Card

Owen Pelham 07813 592 640

Liam Fenwick 07751 286 419

operations@kmsecuritysystems.co.uk

Intruder Alarms
CCTV
Access Control

Colors
f78f20
000000
ffffff

Requirements
Must have
• Must have the logo on the business card somewhere

```html
<!DOCTYPE html>
<html lang="en">
<head>
<meta charset="utf-8">
<title>K M Security Systems – Business Card</title>
<link href="https://fonts.googleapis.com/css2?family=Open+Sans:wght@400;600;700&display=swap" rel="stylesheet">
<style>
  :root {
    --orange: #ff4d0a;
    --black: #000000;
    --white: #ffffff;
    --backdrop: #3a3a3a;
    --backdrop-edge: #1f1f1f;
  }
  * { box-sizing: border-box; margin: 0; padding: 0; }
  html, body { width: 1200px; height: 900px; overflow: hidden; }
  body {
    background: radial-gradient(ellipse at 60% 55%, var(--backdrop) 0%, var(--backdrop-edge) 100%);
    font-family: "Open Sans", Arial, sans-serif;
    color: var(--white);
    position: relative;
  }
  .card {
    position: absolute;
    width: 700px;
    height: 400px;
    left: 250px;
    background: var(--black);
    box-shadow: 0 18px 40px rgba(0,0,0,.55);
    overflow: hidden;
  }
  /* Front */
  .card--front { top: 40px; }
  .brand {
    position: absolute;
    left: 0; right: 0; top: 130px;
    display: flex; align-items: center; justify-content: center; gap: 18px;
  }
  .brand__mark { width: 46px; height: 46px; background: var(--orange); flex: none; }
  .brand__name {
    color: var(--orange);
    font-weight: 700;
    font-size: 44px;
    letter-spacing: 1px;
    text-transform: uppercase;
    white-space: nowrap;
  }
  .services {
    position: absolute;
    left: 0; right: 0; top: 262px;
    text-align: center;
    font-size: 19px;
    letter-spacing: .3px;
  }
  .services__sep { color: var(--orange); margin: 0 6px; }

  /* Back */
  .card--back { top: 470px; }
  .card--back .brand {
    left: 48px; right: auto; top: 88px;
    justify-content: flex-start; gap: 10px;
  }
  .card--back .brand__mark { width: 24px; height: 24px; }
  .card--back .brand__name { font-size: 21px; letter-spacing: .3px; }
  .email {
    position: absolute;
    left: 48px; top: 290px;
    font-size: 19px;
  }
  .divider {
    position: absolute;
    left: 400px; top: 60px;
    width: 2px; height: 160px;
    background: var(--orange);
  }
  .contacts {
    position: absolute;
    left: 430px; top: 178px;
    display: flex; flex-direction: column; gap: 20px;
  }
  .contact__name {
    display: flex; align-items: center; gap: 8px;
    color: var(--orange);
    font-weight: 700;
    font-size: 27px;
    line-height: 1.05;
  }
  .contact__icon { width: 18px; height: 18px; flex: none; }
  .contact__phone {
    font-size: 21px;
    padding-left: 26px;
    line-height: 1.2;
  }
  .edge-band {
    position: absolute;
    left: 0; right: 0; bottom: 0;
    height: 9px;
    background: var(--orange);
  }
</style>
</head>
<body>
  <section class="card card--front" aria-label="Business card front">
    <div class="brand">
      <span class="brand__mark"></span>
      <span class="brand__name">K M Security Systems</span>
    </div>
    <p class="services">Intruder Alarms<span class="services__sep">|</span>CCTV<span class="services__sep">|</span>Access Control</p>
  </section>

  <section class="card card--back" aria-label="Business card back">
    <div class="brand">
      <span class="brand__mark"></span>
      <span class="brand__name">K M Security Systems</span>
    </div>
    <p class="email">operations@kmsecuritysystems.co.uk</p>
    <span class="divider"></span>
    <div class="contacts">
      <div class="contact">
        <p class="contact__name">
          <svg class="contact__icon" viewBox="0 0 24 24" aria-hidden="true"><path fill="#ff4d0a" d="M6.6 10.8a15.1 15.1 0 0 0 6.6 6.6l2.2-2.2c.3-.3.7-.4 1-.2 1.1.4 2.3.6 3.6.6.6 0 1 .4 1 1V20c0 .6-.4 1-1 1A17 17 0 0 1 3 4c0-.6.4-1 1-1h3.5c.6 0 1 .4 1 1 0 1.3.2 2.5.6 3.6.1.3 0 .7-.2 1z"/></svg>
          Owen Pelham
        </p>
        <p class="contact__phone">07813 592 640</p>
      </div>
      <div class="contact">
        <p class="contact__name">
          <svg class="contact__icon" viewBox="0 0 24 24" aria-hidden="true"><path fill="#ff4d0a" d="M6.6 10.8a15.1 15.1 0 0 0 6.6 6.6l2.2-2.2c.3-.3.7-.4 1-.2 1.1.4 2.3.6 3.6.6.6 0 1 .4 1 1V20c0 .6-.4 1-1 1A17 17 0 0 1 3 4c0-.6.4-1 1-1h3.5c.6 0 1 .4 1 1 0 1.3.2 2.5.6 3.6.1.3 0 .7-.2 1z"/></svg>
          Liam Fenwick
        </p>
        <p class="contact__phone">07751 286 419</p>
      </div>
    </div>
    <span class="edge-band"></span>
  </section>
</body>
</html>
```